Business card and stationery
Clear Harbour
Project: Business card and stationery
Business card and stationery  -
Creative Brief
Simple
Name Surname
Executive Director
317 Larkmoor Lane, #03 Fenwick Plaza, Country 264519
vantolemu@mailpost.example
www.clearharbour.example.sg
info (name, address, email etc) on the card should be editable for each employee

```html
<!DOCTYPE html>
<html lang="en">
<head>
<meta charset="utf-8">
<title>Clear Harbour — Business Card</title>
<link href="https://fonts.googleapis.com/css2?family=Open+Sans:wght@400;600;700&display=swap" rel="stylesheet">
<style>
  :root {
    --page: #efeae3;
    --card: #ffffff;
    --card-edge: #e2e2e2;
    --brand-blue: #2f6fe0;
    --brand-green: #2fb52a;
    --ink: #3a3a3a;
    --muted: #555;
    --rule: #cfcfcf;
  }
  * { box-sizing: border-box; margin: 0; padding: 0; }
  html, body { width: 1200px; height: 581px; overflow: hidden; }
  body {
    background: var(--page);
    font-family: "Open Sans", Arial, sans-serif;
    color: var(--ink);
    position: relative;
  }
  .card {
    position: absolute;
    top: 149px;
    width: 488px;
    height: 350px;
    background: var(--card);
    border: 1px solid var(--card-edge);
    border-radius: 22px;
    overflow: hidden;
    box-shadow: 0 6px 14px rgba(0,0,0,.18);
  }
  .card--front { left: 91px; }
  .card--back { left: 606px; }

  .edge-art { position: absolute; inset: 0; width: 100%; height: 100%; }

  .brand {
    position: absolute;
    display: flex;
    flex-direction: column;
    align-items: center;
    gap: 8px;
  }
  .brand__dot {
    width: 44px; height: 44px;
    border-radius: 50%;
    background: var(--brand-green);
  }
  .brand__name {
    font-weight: 600;
    font-size: 26px;
    color: var(--brand-blue);
    white-space: nowrap;
    letter-spacing: -0.3px;
  }
  .card--front .brand { left: 46px; top: 118px; width: 200px; }
  .card--back .brand { left: 0; right: 0; top: 102px; }
  .card--back .brand__name { font-size: 31px; }
  .card--back .brand__dot { width: 50px; height: 50px; }

  .divider {
    position: absolute;
    left: 252px; top: 50px;
    width: 1px; height: 250px;
    background: var(--rule);
  }

  .contact { position: absolute; left: 264px; top: 48px; width: 214px; }
  .contact__name { font-size: 19px; font-weight: 700; color: var(--brand-blue); line-height: 1.2; }
  .contact__title { font-size: 12px; font-weight: 600; color: var(--ink); margin-top: 2px; }
  .contact__address { font-size: 12px; color: var(--muted); line-height: 1.55; margin-top: 26px; }
  .contact__list { list-style: none; margin-top: 18px; }
  .contact__list li {
    display: flex; align-items: center; gap: 8px;
    font-size: 12px; color: var(--muted); line-height: 1.75;
    white-space: nowrap;
  }
  .contact__list svg { width: 12px; height: 12px; flex: none; }

  .website {
    position: absolute; left: 0; right: 0; bottom: 30px;
    text-align: center; font-size: 16px; font-weight: 600; color: var(--ink);
  }
</style>
</head>
<body>

<section class="card card--front" aria-label="Business card front">
  <svg class="edge-art" viewBox="0 0 488 350" preserveAspectRatio="none" aria-hidden="true">
    <path d="M0 0 H110 C55 40 30 110 30 175 C30 240 55 310 110 350 H0 Z" fill="var(--brand-blue)"/>
    <path d="M110 0 C55 40 30 110 30 175 C30 240 55 310 110 350" fill="none" stroke="var(--brand-green)" stroke-width="9"/>
  </svg>

  <div class="brand">
    <span class="brand__dot"></span>
    <span class="brand__name">Clear Harbour</span>
  </div>

  <div class="divider"></div>

  <div class="contact">
    <p class="contact__name">Name Surname</p>
    <p class="contact__title">Executive Director</p>
    <p class="contact__address">317 Larkmoor Lane,<br>#03 Fenwick Plaza,<br>Country 264519</p>
    <ul class="contact__list">
      <li>
        <svg viewBox="0 0 16 16"><path d="M4 2 L6.5 2 L7.5 5 L6 6.5 C6.8 8.2 7.8 9.2 9.5 10 L11 8.5 L14 9.5 L14 12 C14 13 13 14 12 14 C7 14 2 9 2 4 C2 3 3 2 4 2Z" fill="var(--brand-blue)"/></svg>
        +65 6100 2040
      </li>
      <li>
        <svg viewBox="0 0 16 16"><rect x="4" y="1" width="8" height="14" rx="1.5" fill="var(--brand-blue)"/><rect x="5.5" y="3" width="5" height="8" fill="#fff"/></svg>
        +65 6100 3050
      </li>
      <li>
        <svg viewBox="0 0 16 16"><circle cx="8" cy="8" r="7.5" fill="var(--brand-blue)"/><rect x="4" y="5" width="8" height="6" fill="#fff"/><path d="M4 5 L8 8.5 L12 5" stroke="var(--brand-blue)" fill="none"/></svg>
        vantolemu@mailpost.example
      </li>
      <li>
        <svg viewBox="0 0 16 16"><circle cx="8" cy="8" r="7.5" fill="var(--brand-blue)"/><circle cx="8" cy="8" r="4.5" fill="none" stroke="#fff"/><path d="M3.5 8 H12.5 M8 3.5 V12.5" stroke="#fff"/></svg>
        www.clearharbour.example
      </li>
    </ul>
  </div>
</section>

<section class="card card--back" aria-label="Business card back">
  <div class="brand">
    <span class="brand__dot"></span>
    <span class="brand__name">Clear Harbour</span>
  </div>
  <p class="website">www.clearharbour.example.sg</p>
</section>

</body>
</html>
```